W.I.Q 'Wadi Ibn Qutub' for General Transportation

this company is a Iraqi based company.
It provides a number of logistics activities such as;
Overland Transportation
High and heavy logistics
Customs clearance
warehousing
Automotive logistics
The company has been registered since 2009.
If you have any other questions please feel free to ask.
Target Market(s)
Automotive
White goods
All Trading sectors
Industry/Entity Type
Automotive

```html
<!DOCTYPE html>
<html lang="en">
<head>
<meta charset="utf-8">
<title>W.I.Q – Wadi Ibn Qutub Transportation</title>
<link href="https://fonts.googleapis.com/css2?family=Open+Sans:wght@400;600;700&family=Roboto:wght@300;400;700&family=Roboto+Condensed:wght@400;700&display=swap" rel="stylesheet">
<style>
:root{
  --page-bg:#0c3470;
  --page-bg-light:#1d57a6;
  --navy:#0b3c7d;
  --blue:#1466b8;
  --green:#4bb648;
  --orange:#f39200;
  --text:#4a4a4a;
  --heading:#3c3c3c;
  --border:#dcdcdc;
  --footer:#222222;
  --footer-text:#bdbdbd;
  --white:#ffffff;
}
*{box-sizing:border-box;margin:0;padding:0}
html,body{width:1140px;height:1200px;overflow:hidden}
body{
  background:
    radial-gradient(ellipse 520px 90px at 300px 0,var(--page-bg-light),transparent 70%),
    radial-gradient(ellipse 520px 90px at 860px 0,var(--page-bg-light),transparent 70%),
    var(--page-bg);
  font-family:"Open Sans",Arial,sans-serif;
  color:var(--text);
  position:relative;
}
.site{position:absolute;left:144px;top:51px;width:852px;height:1134px;background:var(--white)}
.brand{position:absolute;left:22px;top:20px;display:flex;align-items:flex-start;gap:10px}
.brand-square{width:14px;height:14px;background:var(--navy);margin-top:12px}
.brand-name{font-weight:700;font-size:40px;line-height:40px;color:var(--navy);letter-spacing:1px}
.brand-sub{font-size:11px;line-height:13px;color:var(--navy);margin-top:3px}
.call{position:absolute;right:22px;top:30px}
.call-label{font-size:15px;color:#555;line-height:18px}
.call-number{font-size:17px;font-weight:700;color:var(--navy);line-height:20px}
.nav{position:absolute;left:22px;top:98px;display:flex;height:29px}
.nav a{font-size:11.5px;font-weight:700;color:#333;text-decoration:none;padding:0 14px;line-height:29px;text-transform:uppercase}
.nav a.active{background:var(--navy);color:var(--white)}
.slider{position:absolute;left:22px;top:128px;width:809px;height:320px;border:7px solid var(--navy);background:linear-gradient(#ffffff,#f1f1f1);overflow:hidden}
.slider-map{position:absolute;left:60px;top:6px;width:600px;height:270px;background:radial-gradient(ellipse at center,#e6e6e6,transparent 70%)}
.slider-photo{position:absolute;left:325px;top:38px;width:455px;height:250px;background:linear-gradient(160deg,#8fd97d,#4caf3e 55%,#3c8f33);border-radius:4px}
.slider-trolley{position:absolute;left:6px;top:215px;width:90px;height:90px;background:radial-gradient(circle at 50% 45%,#d9b37a,#b98e52 60%,transparent 70%)}
.slider-caption{position:absolute;left:12px;top:75px;width:440px;height:132px;background:linear-gradient(90deg,rgba(255,255,255,.95),rgba(255,255,255,.75));padding:14px 0 0 46px;white-space:nowrap}
.caption-kicker{font-family:"Roboto",Arial,sans-serif;font-weight:300;font-size:25px;color:#777;line-height:28px}
.caption-title{font-family:"Roboto",Arial,sans-serif;font-weight:700;font-size:37px;color:var(--green);line-height:44px;letter-spacing:-.3px}
.caption-line{font-family:"Roboto",Arial,sans-serif;font-size:27px;color:#111;line-height:32px;letter-spacing:-.4px}
.caption-line small{font-size:19px;letter-spacing:-.3px}
.slider-dots{position:absolute;left:360px;bottom:4px;display:flex;gap:4px}
.slider-dots span{width:8px;height:8px;border-radius:50%;background:#d5d5d5}
.slider-dots span.on{background:var(--navy)}
.services{position:absolute;left:22px;top:480px;width:809px;height:176px;border:1px solid var(--border);border-radius:3px;background:linear-gradient(#ffffff,#f0f0f0);display:flex;padding:13px 0 0 13px;gap:23px}
.service{width:138px}
.service-photo{width:138px;height:82px}
.service-title{font-size:11px;font-weight:700;color:var(--blue);margin-top:10px;line-height:14px}
.service-text{font-size:10.5px;line-height:13px;color:#444;margin-top:5px}
.welcome{position:absolute;left:22px;top:682px;width:526px}
.welcome h1{font-size:25px;font-weight:600;color:var(--heading);line-height:30px}
.welcome h1 span{color:var(--blue)}
.welcome p{font-size:10.8px;line-height:15.7px;color:#555;margin-top:2px}
.welcome p + p{margin-top:15px}
.quote{position:absolute;left:606px;top:689px;width:221px;height:250px;background:linear-gradient(#ffffff,#e9e9e9);border:1px solid var(--border);border-radius:5px}
.quote-head{position:relative;height:38px;background:var(--navy);border-radius:5px 5px 0 0;color:var(--white);font-size:17px;text-align:center;line-height:38px}
.quote-head b{color:#ffd200}
.quote-head::after{content:"";position:absolute;left:50%;bottom:-9px;margin-left:-9px;border-left:9px solid transparent;border-right:9px solid transparent;border-top:9px solid var(--navy)}
.quote-form{padding:20px 0 0 15px}
.quote-field{width:190px;height:29px;background:var(--white);border:1px solid #e3e3e3;font-size:10.5px;color:#999;line-height:27px;padding-left:8px;margin-bottom:6px}
.quote-submit{display:inline-block;margin-top:6px;background:linear-gradient(#ffa92b,var(--orange));color:var(--white);font-weight:700;font-size:14px;padding:3px 12px;border-radius:3px}
.footer{position:absolute;left:138px;top:1020px;width:864px;height:135px;background:var(--footer);color:var(--footer-text)}
.footer h3{font-size:13px;font-weight:600;color:var(--white);line-height:16px}
.links{position:absolute;left:28px;top:21px}
.links ul{list-style:none;position:absolute;top:27px;width:120px}
.links li{font-size:10.5px;line-height:19px;white-space:nowrap}
.links li::before{content:"›";color:#777;margin-right:7px}
.contact{position:absolute;left:314px;top:21px}
.contact-address{position:absolute;left:0;top:27px;display:flex;gap:12px;width:170px}
.contact-address p{font-size:10.5px;line-height:16px}
.contact-phone{position:absolute;left:510px;top:46px;display:flex;gap:6px}
.phone-number{font-family:"Roboto Condensed",Arial,sans-serif;font-weight:700;font-size:21px;color:var(--white);line-height:22px;letter-spacing:.5px}
.phone-mail{font-size:11px;color:#f2b600;line-height:16px}
.social{position:absolute;left:728px;top:21px}
.social-icons{display:flex;gap:6px;margin-top:15px}
.social-icons span{width:31px;height:31px;border-radius:50%;background:#5c5c5c}
.legal{position:absolute;left:144px;top:1155px;width:852px;height:30px;background:var(--white);font-size:10.5px;color:#555;line-height:30px;padding:0 22px;display:flex;justify-content:space-between}
.legal nav span{margin:0 9px;color:#999}
</style>
</head>
<body>
<div class="site">
  <header>
    <div class="brand">
      <div class="brand-square"></div>
      <div>
        <div class="brand-name">W.I.Q</div>
        <div class="brand-sub">Wadi Ibn Qutub<br>Transportation</div>
      </div>
    </div>
    <div class="call">
      <div class="call-label">Call Now</div>
      <div class="call-number">(012) 555-0148</div>
    </div>
    <nav class="nav">
      <a class="active">Home</a><a>About Us</a><a>Services</a><a>Industries</a><a>Case Studies</a><a>News and Events</a><a>Contact Us</a>
    </nav>
  </header>

  <section class="slider">
    <div class="slider-map" role="img" aria-label="Faint dotted world map"></div>
    <div class="slider-photo" role="img" aria-label="Green shipping container printed with a world map"></div>
    <div class="slider-trolley" role="img" aria-label="Hand truck carrying import boxes"></div>
    <div class="slider-caption">
      <div class="caption-kicker">Lorem Ipsum</div>
      <div class="caption-title">Simply dummy text</div>
      <div class="caption-line">Lorem Ipsum <small>Printing and Typesetting</small></div>
    </div>
    <div class="slider-dots"><span class="on"></span><span></span><span></span><span></span><span></span><span></span></div>
  </section>

  <section class="services">
    <article class="service">
      <div class="service-photo" role="img" aria-label="Green truck in front of stacked containers" style="background:linear-gradient(#c9d8e8,#6aa35c 60%,#c0453a)"></div>
      <h2 class="service-title">Overland Transportation</h2>
      <p class="service-text">Lorem Ipsum is simply dummy text of the printing and typesetting industry.</p>
    </article>
    <article class="service">
      <div class="service-photo" role="img" aria-label="Container port with cranes" style="background:linear-gradient(#3a7cc4,#d85a3c 60%,#2f5f9a)"></div>
      <h2 class="service-title">High and Heavy Logistics</h2>
      <p class="service-text">Lorem Ipsum is simply dummy text of the printing and typesetting industry.</p>
    </article>
    <article class="service">
      <div class="service-photo" role="img" aria-label="Customs officer with a clipboard" style="background:linear-gradient(90deg,#8a6a4a,#c8d6e6 60%,#9a7a5a)"></div>
      <h2 class="service-title">Customs Clearance</h2>
      <p class="service-text">Lorem Ipsum is simply dummy text of the printing and typesetting industry.</p>
    </article>
    <article class="service">
      <div class="service-photo" role="img" aria-label="Warehouse shelves with boxes" style="background:linear-gradient(#b08454,#d8b58a 50%,#8a6440)"></div>
      <h2 class="service-title">warehousing</h2>
      <p class="service-text">Lorem Ipsum is simply dummy text of the printing and typesetting industry.</p>
    </article>
    <article class="service">
      <div class="service-photo" role="img" aria-label="Row of white trucks" style="background:linear-gradient(#7aa6d6,#e8e8e8 55%,#6a6a6a)"></div>
      <h2 class="service-title">Automotive Logistics</h2>
      <p class="service-text">Lorem Ipsum is simply dummy text of the printing and typesetting industry.</p>
    </article>
  </section>

  <section class="welcome">
    <h1>Welcome to <span>WIQ</span></h1>
    <p>Lorem Ipsum is simply dummy text of the printing and typesetting industry. Lorem Ipsum has been the industry's standard dummy text ever since the 1500s, when an unknown printer took a galley of type and scrambled it to make a type specimen book. It has survived not only five centuries, but also the leap into electronic typesetting, remaining essentially unchanged. It was popularised in the 1960s with the release of Letraset sheets containing Lorem Ipsum passages, and more recently It has survived not only five centuries, but also the leap into electronic typesetting, remaining essentially unchanged with desktop publishing software like Aldus PageMaker including versions of Lorem Ipsum.</p>
    <p>There are many variations of passages of Lorem Ipsum available, but the majority have suffered alteration in some form, by injected humour, or randomised words which don't look even slightly believable. If you are going to use a passage of Lorem Ipsum, you need to be sure there isn't anything embarrassing hidden in the middle of text. All the Lorem Ipsum generators on the Internet tend to repeat predefined chunks as necessary, making this the first true generator on the Internet. It uses a dictionary of over 200 Latin words, combined non-characteristic words etc.</p>
  </section>

  <aside class="quote">
    <div class="quote-head">Get a <b>FREE</b> Quote</div>
    <div class="quote-form">
      <div class="quote-field">Enter Your Name</div>
      <div class="quote-field">Enter Your Email</div>
      <div class="quote-field">Phone number</div>
      <div class="quote-field">Zip Code</div>
      <div class="quote-submit">Submit</div>
    </div>
  </aside>
</div>

<footer class="footer">
  <div class="links">
    <h3>Quick Links</h3>
    <ul style="left:0"><li>Home</li><li>About Us</li><li>Services</li><li>Industries</li></ul>
    <ul style="left:127px"><li>Case Studies</li><li>News and Events</li><li>Contact Us</li></ul>
  </div>
  <div class="contact">
    <h3>Quick Contect</h3>
    <div class="contact-address">
      <svg width="12" height="16" viewBox="0 0 12 16" aria-hidden="true"><path d="M6 0a6 6 0 0 0-6 6c0 4.5 6 10 6 10s6-5.5 6-10a6 6 0 0 0-6-6z" fill="#777"/><circle cx="6" cy="6" r="2.3" fill="#222"/></svg>
      <p>121 Lorem Ipsum is simply dummy text of the printing and typesetting industry</p>
    </div>
  </div>
  <div class="contact-phone">
    <svg width="12" height="32" viewBox="0 0 12 32" aria-hidden="true"><path d="M9 0H4C1 0 0 6 0 16s1 16 4 16h5v-9H5c-1-3-1-11 0-14h4z" fill="#777"/></svg>
    <div>
      <div class="phone-number">012.555.0148</div>
      <div class="phone-mail">info@wiqtransport.com</div>
    </div>
  </div>
  <div class="social">
    <h3>Let's Contect</h3>
    <div class="social-icons"><span></span><span></span><span></span></div>
  </div>
</footer>

<div class="legal">
  <span>© 2014 Wadi Ibn Qutub. All Rights Reserved.</span>
  <nav>Privacy Policy<span>|</span>Disclaimer</nav>
</div>
</body>
</html>
```